BRIGHTPINE RV Resort needs a logo and advertising poster

We need an advertising poster for our epic RV Resort located on north end of Tolvin Lake, (Northern Saskatchewan, trees no mountains)
SEASONAL FULL SERVICE SITES with marina and lake access.
Sauna/plunge, disc golf , hiking/quad trails, and pet friendly.
We are after a fun 70,s themed simple poster. Please use brand guide for colours and redo logo to be Brightpine Resort.

Target Market(s)

RV owners looking for permeant sites. No tenting.

Font styles to use
Other font styles liked:
• See brand guide

Requirements
Must have
• Change exisiting branding to BRIGHTPINE RESORT instead of coffee Emphasis Limited sites.... Referral discount. Phone number.
Nice to have
• .
Should not have
• Keep it simple

```html
<!DOCTYPE html>
<html lang="en">
<head>
<meta charset="utf-8">
<title>Fern Bay Resort and Marina – Seasonal Sites</title>
<link rel="stylesheet" href="https://fonts.googleapis.com/css2?family=Roboto+Condensed:wght@700;800;900&family=Arimo:wght@400;700&display=swap">
<style>
  :root {
    --forest: #3e5029;
    --moss: #6a8252;
    --cream: #faf7ec;
    --sand: #e9cb72;
    --mustard: #d4ac40;
    --lake: #7bad8a;
    --head: "Roboto Condensed", "Arial Narrow", sans-serif;
    --body: "Arimo", Arial, sans-serif;
  }
  * { box-sizing: border-box; margin: 0; padding: 0; }
  html, body { width: 884px; height: 1200px; overflow: hidden; background: var(--moss); }
  .poster { position: relative; width: 884px; height: 1200px; background: var(--moss); }
  .sheet {
    position: absolute; left: 75px; top: 80px; width: 733px; height: 1037px;
    background: var(--cream); overflow: hidden;
  }
  .brand {
    position: absolute; left: 44px; top: 118px; width: 150px;
    font-family: var(--head); font-weight: 800; color: var(--forest);
    font-size: 25px; line-height: 1.05; text-align: center; letter-spacing: 0.5px;
  }
  .title {
    position: absolute; left: 255px; top: 28px;
    font-family: var(--head); font-weight: 900; color: var(--forest);
    font-size: 62px; line-height: 72px; letter-spacing: 0.5px;
  }
  .tagline {
    position: absolute; left: 255px; top: 176px; width: 450px;
    font-family: var(--body); color: var(--forest); font-size: 15px; line-height: 20px;
  }
  .scene {
    position: absolute; left: 0; top: 220px; width: 733px; height: 480px;
    background: linear-gradient(180deg, var(--cream) 0%, #b9c69a 18%, var(--moss) 40%, var(--lake) 60%, var(--lake) 66%, var(--sand) 74%, var(--sand) 100%);
  }
  .ground { position: absolute; left: 0; top: 620px; width: 733px; height: 417px; background: var(--sand); }
  .section-head {
    position: absolute; left: 0; top: 610px; width: 733px; text-align: center;
    font-family: var(--head); font-weight: 800; color: var(--forest);
    font-size: 35px; letter-spacing: 0.3px;
  }
  .swoosh { position: absolute; top: 618px; width: 52px; height: 36px; }
  .swoosh.left { left: 78px; }
  .swoosh.right { left: 598px; }
  .amenities {
    position: absolute; left: 47px; top: 664px; width: 639px; height: 152px;
    background: var(--mustard); border-radius: 26px 0 26px 26px;
  }
  .amenity { position: absolute; top: 14px; width: 140px; margin-left: -70px; text-align: center; }
  .amenity svg { display: block; margin: 0 auto; width: 70px; height: 74px; }
  .amenity-label {
    margin-top: 6px; font-family: var(--body); font-weight: 700; color: var(--forest);
    font-size: 16px; line-height: 20px;
  }
  .referral {
    position: absolute; left: 48px; top: 850px; width: 152px; height: 147px;
    background: var(--mustard); border-radius: 26px 0 26px 26px; color: var(--cream);
    font-family: var(--head); font-weight: 800; text-align: left; padding: 16px 0 0 39px;
  }
  .referral-rate { font-size: 72px; line-height: 66px; }
  .referral-rate span { font-size: 42px; }
  .referral-label { font-size: 18px; line-height: 17px; margin-top: 6px; }
  .limited {
    position: absolute; left: 275px; top: 860px;
    font-family: var(--head); font-weight: 900; color: var(--forest); font-size: 56px; line-height: 60px;
  }
  .phone {
    position: absolute; left: 222px; top: 930px; display: flex; align-items: center; gap: 14px;
    font-family: var(--head); font-weight: 900; color: var(--forest); font-size: 70px; line-height: 76px;
  }
  .phone svg { width: 40px; height: 40px; }
</style>
</head>
<body>
<main class="poster">
  <section class="sheet">
    <div class="brand">BRIGHTPINE<br>RESORT</div>
    <h1 class="title">FERN BAY RESORT<br>AND MARINA</h1>
    <p class="tagline">Epic Campground, Located on north end of Tolvin Lake, Northern Saskatchewan</p>

    <div class="scene" role="img" aria-label="Illustration of a vintage travel trailer parked on a sandy lakeshore with pine trees and a setting sun behind"></div>
    <div class="ground"></div>

    <svg class="swoosh left" viewBox="0 0 52 36" aria-hidden="true">
      <path d="M50 8 C34 0 18 4 10 22" fill="none" stroke="var(--cream)" stroke-width="5" stroke-linecap="round"/>
      <path d="M2 16 L8 34 L22 24 Z" fill="var(--cream)"/>
    </svg>
    <h2 class="section-head">SEASONAL FULL SERVICE SITE</h2>
    <svg class="swoosh right" viewBox="0 0 52 36" aria-hidden="true">
      <path d="M2 8 C18 0 34 4 42 22" fill="none" stroke="var(--cream)" stroke-width="5" stroke-linecap="round"/>
      <path d="M50 16 L44 34 L30 24 Z" fill="var(--cream)"/>
    </svg>

    <div class="amenities">
      <div class="amenity" style="left:88px">
        <svg viewBox="0 0 70 74" aria-hidden="true">
          <path d="M33 4 L33 56 L10 56 Z M37 14 L37 56 L60 56 Z" fill="var(--cream)"/>
          <path d="M4 60 L66 60 C62 70 56 72 46 72 L20 72 C12 72 7 68 4 60 Z" fill="var(--cream)"/>
        </svg>
        <div class="amenity-label">MARINA AND<br>LAKE ACCESS</div>
      </div>
      <div class="amenity" style="left:217px">
        <svg viewBox="0 0 70 74" aria-hidden="true">
          <g fill="none" stroke="var(--cream)" stroke-width="3" stroke-linecap="round">
            <path d="M22 34 C16 28 28 24 22 16 C18 10 26 8 22 4"/>
            <path d="M35 34 C29 28 41 24 35 16 C31 10 39 8 35 4"/>
            <path d="M48 34 C42 28 54 24 48 16 C44 10 52 8 48 4"/>
          </g>
          <rect x="4" y="44" width="62" height="8" rx="3" fill="var(--cream)"/>
          <rect x="8" y="50" width="54" height="22" rx="4" fill="var(--cream)"/>
        </svg>
        <div class="amenity-label">SAUNA/<br>PLUNGE</div>
      </div>
      <div class="amenity" style="left:314px">
        <svg viewBox="0 0 70 74" aria-hidden="true">
          <g fill="none" stroke="var(--cream)" stroke-width="3">
            <rect x="15" y="6" width="40" height="8" fill="var(--cream)"/>
            <path d="M19 14 L30 40 M27 14 L33 40 M35 14 L35 40 M43 14 L37 40 M51 14 L40 40"/>
            <path d="M14 42 L56 42 L50 56 L20 56 Z"/>
            <path d="M35 42 L35 72"/>
          </g>
        </svg>
        <div class="amenity-label">DISC<br>GOLF</div>
      </div>
      <div class="amenity" style="left:433px">
        <svg viewBox="0 0 70 74" aria-hidden="true">
          <circle cx="40" cy="10" r="7" fill="var(--cream)"/>
          <path d="M30 22 L42 22 L48 38 L58 38 L58 44 L44 44 L38 34 L34 46 L30 54 L24 52 L28 40 Z" fill="var(--cream)"/>
          <rect x="20" y="22" width="8" height="16" rx="2" fill="var(--cream)"/>
          <g fill="none" stroke="var(--cream)" stroke-width="4">
            <circle cx="16" cy="58" r="11"/><circle cx="56" cy="58" r="11"/>
          </g>
        </svg>
        <div class="amenity-label">HIKING/QUAD<br>TRAILS</div>
      </div>
      <div class="amenity" style="left:567px">
        <svg viewBox="0 0 70 74" aria-hidden="true">
          <g fill="var(--cream)">
            <ellipse cx="10" cy="28" rx="7" ry="9"/><ellipse cx="24" cy="12" rx="7" ry="10"/>
            <ellipse cx="46" cy="12" rx="7" ry="10"/><ellipse cx="60" cy="28" rx="7" ry="9"/>
            <path d="M35 32 C22 32 14 48 16 60 C18 70 28 64 35 64 C42 64 52 70 54 60 C56 48 48 32 35 32 Z"/>
          </g>
          <path d="M27 50 L33 56 L44 44" fill="none" stroke="var(--mustard)" stroke-width="4" stroke-linecap="round"/>
        </svg>
        <div class="amenity-label">PET<br>FRIENDLY</div>
      </div>
    </div>

    <div class="referral">
      <div class="referral-rate">5<span>%</span></div>
      <div class="referral-label">REFERRAL<br>DISCOUNT</div>
    </div>

    <div class="limited">LIMITED SITES</div>
    <div class="phone">
      <svg viewBox="0 0 40 40" aria-hidden="true">
        <path d="M4 6 L12 2 L18 12 L13 16 C15 22 19 26 25 28 L29 23 L38 30 L34 38 C18 38 4 24 4 6 Z" fill="var(--forest)"/>
      </svg>
      <span>855-555-0142</span>
    </div>
  </section>
</main>
</body>
</html>
```